Every sort of trades everysortoftrades.ca

Website for company offering Every sort of trades
Welding/Fabrication/Metal repairs/Metal building, Electrical repairs and installations, Plumbing and Heating, Renovations, Flooring, Paiting, and other services

We need a very clean and professional website outlining the many services we have

We would like each type of service to have its own page, with images of those types of services on those pages.

Then in the future, we can update those pages with projects we have done of those types.

Every Sort of Trades . CA

Located in Calgary, Alberta, Canada, offering services Alberta wide

Welding/Fabrication/Repair/Building - Steel and metals
Electrical contractor - Journeyman , small or large projects
Plumbing and Heating
Renovations
Flooring
Painting
Other services - storage, trucking, delivery, etc

business and residential services

Contractor

5+ page

Sans Serif

3176b5
0253a1
85acd3
85abd2
cedeed
ffffff

Must have
• Clean
• Professional
• Easy of updating text and images

```html
<!DOCTYPE html>
<html lang="en">
<head>
<meta charset="utf-8">
<title>Every Sort of Trades</title>
<link rel="stylesheet" href="https://fonts.googleapis.com/css2?family=Montserrat:wght@400;500;600;700&family=Open+Sans:wght@400;600&display=swap">
<style>
:root{
  --blue:#0253a1;
  --blue-mid:#3176b5;
  --blue-soft:#85acd3;
  --blue-pale:#cedeed;
  --white:#ffffff;
  --ink:#555c66;
  --dark:#1a1c20;
  --line:#d9dde2;
}
*{margin:0;padding:0;box-sizing:border-box}
html,body{width:1200px;height:2332px;overflow:hidden;background:var(--white)}
body{position:relative;font-family:"Open Sans",Arial,sans-serif;color:var(--ink)}
.abs{position:absolute}
.heading{font-family:"Montserrat",Arial,sans-serif;font-weight:700;color:var(--blue);text-align:center;letter-spacing:1px}

/* hero */
.hero{left:0;top:0;width:1200px;height:620px;background:radial-gradient(ellipse at 30% 70%,#5b7fa0 0%,#2b3b4c 35%,#121619 75%),#111}
.hero-glow{left:0;top:0;width:1200px;height:620px;background:radial-gradient(circle at 22% 72%,rgba(255,190,120,.35),transparent 30%),radial-gradient(circle at 72% 82%,rgba(255,170,80,.3),transparent 25%)}
.nav{left:0;top:0;width:1200px;height:65px;background:rgba(40,40,42,.82)}
.brand{left:100px;top:20px;font-family:"Montserrat",Arial,sans-serif;font-weight:700;font-size:19px;color:var(--white);letter-spacing:.5px}
.nav-link{top:24px;font-family:"Montserrat",Arial,sans-serif;font-weight:600;font-size:13px;color:var(--white);text-transform:uppercase}
.nav-active{left:521px;top:60px;width:66px;height:5px;background:var(--blue-mid)}
.hero-title{left:0;top:266px;width:1200px;text-align:center;font-family:"Montserrat",Arial,sans-serif;font-weight:700;font-size:50px;color:var(--white);letter-spacing:1.5px}
.hero-sub{left:200px;top:358px;width:800px;text-align:center;font-family:"Montserrat",Arial,sans-serif;font-weight:700;font-size:25px;line-height:41px;color:var(--white);text-transform:uppercase}

/* cta band */
.cta{left:0;top:620px;width:1200px;height:95px;background:var(--blue)}
.cta-text{left:160px;top:653px;font-family:"Montserrat",Arial,sans-serif;font-weight:500;font-size:21px;color:var(--white)}
.cta-btn{left:843px;top:650px;width:195px;height:36px;border:2px dashed var(--white);color:var(--white);font-family:"Montserrat",Arial,sans-serif;font-weight:600;font-size:15px;text-align:center;line-height:32px;text-transform:uppercase}

/* welcome */
.welcome-title{left:0;top:772px;width:1200px;font-size:34px}
.welcome-lead{left:179px;top:830px;width:842px;font-size:12px;line-height:21.5px;text-align:center}
.welcome-photo{left:172px;top:931px;width:402px;height:229px;background:linear-gradient(180deg,#c9ccd0 0%,#b8bcc1 45%,#c6a17a 60%,#d9b98f 100%)}
.welcome-copy{left:616px;top:948px;width:435px;font-size:12px;line-height:21px;text-align:justify}
.welcome-list{left:616px;top:1048px;width:435px;list-style:none;font-size:12px;line-height:26px}
.welcome-list li::before{content:"";display:inline-block;width:6px;height:6px;border-radius:50%;background:var(--ink);margin-right:8px;vertical-align:middle}

/* services */
.services{left:0;top:1217px;width:1200px;height:473px;background:linear-gradient(135deg,#0a5bb0 0%,#0253a1 40%,#0f5cab 60%,#0253a1 100%)}
.services-title{left:0;top:1259px;width:1200px;font-size:34px;color:var(--white)}
.services-sub{left:190px;top:1320px;width:820px;text-align:center;font-size:14px;line-height:21px;color:var(--white)}
.card{width:221px;height:227px;top:1419px;border:1px solid var(--blue-soft);color:var(--white);text-align:center}
.card-icon{position:absolute;left:81px;top:-30px;width:60px;height:60px;border-radius:50%;background:var(--blue);border:2px solid var(--white)}
.card-icon svg{position:absolute;left:15px;top:15px}
.card-title{margin-top:56px;font-family:"Montserrat",Arial,sans-serif;font-weight:700;font-size:17px;letter-spacing:.5px}
.card-text{margin:20px 17px 0;font-size:12.5px;line-height:21px;text-align:justify;text-align-last:center}

/* blog */
.blog-title{left:0;top:1720px;width:1200px;font-size:34px}
.post{top:1804px;width:423px;height:187px;border:2px solid #e6e8eb;background:var(--white)}
.post-name{font-family:"Montserrat",Arial,sans-serif;font-weight:700;font-size:17px;color:var(--blue);letter-spacing:.5px}
.post-text{font-size:12px;line-height:21px;margin-top:6px}
.avatar{width:92px;height:92px;border-radius:50%;top:1841px}
.arrow{top:1881px;width:30px;height:32px;background:var(--blue-soft)}
.arrow svg{position:absolute;left:8px;top:9px}

/* follow */
.follow{left:0;top:2039px;width:1200px;height:249px;background:linear-gradient(90deg,#6d5a4c 0%,#3f3a38 35%,#222a35 65%,#2e3c50 100%)}
.follow-shade{left:0;top:2039px;width:1200px;height:249px;background:rgba(10,15,25,.35)}
.follow-title{left:0;top:2099px;width:1200px;text-align:center;font-family:"Montserrat",Arial,sans-serif;font-weight:500;font-size:34px;color:var(--white)}
.social{top:2181px;width:46px;height:46px;border-radius:50%;border:2px solid var(--white)}

/* footer */
.footer{left:0;top:2288px;width:1200px;height:44px;background:var(--blue);color:var(--white);text-align:center;font-size:13px;font-weight:600;line-height:44px}
</style>
</head>
<body>

<div class="abs hero" role="img" aria-label="Welders at work with sparks flying in a dark workshop"></div>
<div class="abs hero-glow"></div>

<header>
  <div class="abs nav"></div>
  <div class="abs brand">EVERY SORT OF TRADES</div>
  <nav>
    <span class="abs nav-link" style="left:532px">Home</span>
    <span class="abs nav-link" style="left:617px">About Us</span>
    <span class="abs nav-link" style="left:735px">Services</span>
    <span class="abs nav-link" style="left:849px">Blog</span>
    <span class="abs nav-link" style="left:925px">Team</span>
    <span class="abs nav-link" style="left:1012px">Contact Us</span>
  </nav>
  <div class="abs nav-active"></div>
</header>

<h1 class="abs hero-title">BEST SERVICE AT LOW PRICE</h1>
<p class="abs hero-sub">Located in Calgary, Alberta, Canada, offering<br>services Alberta wide</p>

<section>
  <div class="abs cta"></div>
  <p class="abs cta-text">Our Team Will Provide A High Quality For Service</p>
  <div class="abs cta-btn">Contact Us</div>
</section>

<section>
  <h2 class="abs heading welcome-title">WELCOME</h2>
  <p class="abs welcome-lead">Lorem Ipsum is simply dummy text of the printing and typesetting industry. Lorem Ipsum has been the industry's standard dummy text ever since the 1500s, when an unknown printer took a galley of type and scrambled it to make a type specimen book. It has survived not only five centuries, but also the leap into electronic typesetting, remaining essentially unchanged.</p>
  <div class="abs welcome-photo" role="img" aria-label="Tradesman kneeling to install a wooden floor in a bright room"></div>
  <p class="abs welcome-copy">Lorem Ipsum is simply dummy text of the printing and typesetting industry. Lorem Ipsum has been the industry's standard dummy text ever since the 1500s, when an unknown printerally unchanged. standard dummy text ever since the 1500s, when an unknown printerally unchanged.</p>
  <ul class="abs welcome-list">
    <li>Electrical repairs and installations</li>
    <li>Plumbing and Heating</li>
    <li>Emergency power solutions (generators)</li>
    <li>Virtually any electrical needs you have – just ask!</li>
  </ul>
</section>

<section>
  <div class="abs services" role="img" aria-label="Blue background with soft diagonal shapes"></div>
  <h2 class="abs heading services-title">SERVICES</h2>
  <p class="abs services-sub">Welding/Fabrication/Metal repairs/Metal building, Electrical repairs and installations, Plumbing and Heating, Renovations, Flooring, Paiting, and other services</p>

  <div class="abs card" style="left:90px">
    <div class="card-icon"><svg width="26" height="26" viewBox="0 0 26 26"><path d="M20 3l3 3-9 9-3-3z" fill="#fff"/><path d="M10 13l3 3c-1 4-5 6-9 6 1-2 1-5 3-7z" fill="#fff"/></svg></div>
    <div class="card-title">PAINTING</div>
    <p class="card-text">Lorem Ipsum is simply dummy text of the printing and typesetting industry.orem Ipsum is simply dummy text of the printing and typesetting industry</p>
  </div>
  <div class="abs card" style="left:356px">
    <div class="card-icon"><svg width="26" height="26" viewBox="0 0 26 26"><circle cx="13" cy="13" r="8" fill="none" stroke="#fff" stroke-width="4" stroke-dasharray="4 2.3"/><circle cx="13" cy="13" r="3" fill="#fff"/></svg></div>
    <div class="card-title">RENOVATIONS</div>
    <p class="card-text">Lorem Ipsum is simply dummy text of the printing and typesetting industry.orem Ipsum is simply dummy text of the printing and typesetting industry</p>
  </div>
  <div class="abs card" style="left:625px">
    <div class="card-icon"><svg width="26" height="26" viewBox="0 0 26 26"><path d="M13 3l9 6-9 6-9-6z M4 14l9 6 9-6" fill="none" stroke="#fff" stroke-width="2.2" stroke-linejoin="round"/></svg></div>
    <div class="card-title">FLOORING</div>
    <p class="card-text">Lorem Ipsum is simply dummy text of the printing and typesetting industry.orem Ipsum is simply dummy text of the printing and typesetting industry</p>
  </div>
  <div class="abs card" style="left:889px">
    <div class="card-icon"><svg width="26" height="26" viewBox="0 0 26 26"><rect x="4" y="8" width="14" height="6" fill="#fff"/><rect x="9" y="4" width="3" height="4" fill="#fff"/><rect x="6" y="3" width="9" height="2" fill="#fff"/><path d="M18 8h3v10h-3z" fill="#fff"/><circle cx="19.5" cy="22" r="1.5" fill="#fff"/></svg></div>
    <div class="card-title">PLUMBING &amp; HEATING</div>
    <p class="card-text">Lorem Ipsum is simply dummy text of the printing and typesetting industry.orem Ipsum is simply dummy text of the printing and typesetting industry</p>
  </div>
</section>

<section>
  <h2 class="abs heading blog-title">OUR BLOG</h2>
  <div class="abs arrow" style="left:103px"><svg width="14" height="14" viewBox="0 0 14 14"><path d="M10 1L4 7l6 6" fill="none" stroke="#fff" stroke-width="2"/></svg></div>

  <article class="abs post" style="left:117px;padding:36px 60px 0 34px;text-align:right">
    <div class="post-name">MARA HOLT</div>
    <p class="post-text" style="text-align:justify;text-align-last:right">Lorem Ipsum is simply dummy text of the printing and typesetting industry. Lorem Ipsum has been the industry's standard dummy text ever since the 1500s.Lorem Ipsum is simply dummy text of the printing and typesetting</p>
  </article>
  <div class="abs avatar" style="left:494px;background:linear-gradient(160deg,#c9dfe3,#7fa6a8)" role="img" aria-label="Blog author portrait"></div>

  <article class="abs post" style="left:653px;padding:36px 34px 0 62px">
    <div class="post-name">THEO LUND</div>
    <p class="post-text" style="text-align:justify">Lorem Ipsum is simply dummy text of the printing and typesetting industry. Lorem Ipsum has been the industry's standard dummy text ever since the 1500s.Lorem Ipsum is simply dummy text of the printing and typesetting</p>
  </article>
  <div class="abs avatar" style="left:607px;background:radial-gradient(circle at 50% 40%,#f0b24a,#b8641c 55%,#3a2410)" role="img" aria-label="Sunset sky with birds in flight"></div>

  <div class="abs arrow" style="left:1063px"><svg width="14" height="14" viewBox="0 0 14 14"><path d="M4 1l6 6-6 6" fill="none" stroke="#fff" stroke-width="2"/></svg></div>
</section>

<section>
  <div class="abs follow" role="img" aria-label="Hands tightening a tap with a wrench beside a running shower head"></div>
  <div class="abs follow-shade"></div>
  <h2 class="abs follow-title">Follow Us</h2>
  <div class="abs social" style="left:465px" aria-label="Social profile"></div>
  <div class="abs social" style="left:540px" aria-label="Social profile"></div>
  <div class="abs social" style="left:611px" aria-label="Social profile"></div>
  <div class="abs social" style="left:687px" aria-label="Social profile"></div>
</section>

<footer class="abs footer">© 2017 Every Sort of Trades &nbsp;All right reserved &nbsp;Term of Use</footer>

</body>
</html>
```